FUNDRAISER FLYER For Tshirt Business

I would like a front and back flyer advertising fundraising for my print on demand business(LANTERN PRINT CO) I would like an eye catching color scheme. I don't want it to be cluttered the font should be bold. I am attaching a list of things I need included, please use this as informational that I need on the flyer but not for direction and style. Quick turnaround time. Please add our Instagram and FB info to Flyer with Contact Info

Target Market(s)

Organizations looking to add to their capital by doing fundraising.

Industry/Entity Type

Organization

Requirements
Must have
• Information provided make sure the packages is easily defined
Nice to have
• A key information
Should not have
• Do not copy the images provided. I didn’t not like this layout.

```html
<!DOCTYPE html>
<html lang="en">
<head>
<meta charset="utf-8">
<title>Lantern Print Co – Fundraiser Flyer</title>
<link rel="stylesheet" href="https://fonts.googleapis.com/css2?family=Anton&family=Oswald:wght@500;600&family=Montserrat:wght@500;600;700;800;900&family=Dancing+Script:wght@700&display=swap">
<style>
  :root {
    --red: #c8102e;
    --yellow: #ffc20e;
    --ink: #1c1c1c;
    --white: #ffffff;
    --rule: #c99a2e;
  }
  * { box-sizing: border-box; margin: 0; padding: 0; }
  html, body { width: 1200px; height: 1200px; overflow: hidden; background: var(--white); }
  body { position: relative; font-family: "Montserrat", sans-serif; color: var(--ink); }

  .flyer {
    position: absolute; top: 235px; width: 495px; height: 700px;
    background: var(--white); overflow: hidden;
  }
  .flyer--front { left: 94px; }
  .flyer--back { left: 634px; }
  .flyer__bg { position: absolute; inset: 0; width: 100%; height: 100%; }

  /* Front header */
  .headline {
    position: absolute; left: 29px; top: 30px;
    font-family: "Anton", sans-serif; font-size: 43px; line-height: 43px;
    color: var(--white); letter-spacing: 1.6px;
  }
  .headline__accent { color: var(--yellow); letter-spacing: 1.9px; }
  .hero-shirts {
    position: absolute; left: 272px; top: 15px; width: 218px; height: 181px;
    border-radius: 40px 40px 12px 12px;
    background: linear-gradient(100deg, #f4f4f4 0 55%, #2a2a2a 55% 100%);
  }

  /* Packages */
  .package { position: absolute; left: 0; width: 100%; }
  .package--silver { top: 222px; }
  .package--gold { top: 340px; }
  .package--platinum { top: 459px; }

  .tier {
    position: absolute; left: 32px; top: 0; height: 32px;
    padding: 0 22px; display: flex; align-items: center;
    font-size: 24px; font-weight: 600; color: var(--white);
    clip-path: polygon(4% 10%, 100% 0, 96% 50%, 100% 100%, 2% 92%, 0 50%);
  }
  .tier--silver { width: 148px; background: linear-gradient(90deg, #9a9a9a, #eeeeee 50%, #a8a8a8); }
  .tier--gold { width: 148px; background: linear-gradient(90deg, #b08a3a, #d9b76a 50%, #a67f2e); }
  .tier--platinum { width: 188px; background: linear-gradient(90deg, #3c3c3c, #7a7a7a 50%, #4a4a4a); }

  .features {
    position: absolute; left: 31px; top: 52px; list-style: none;
    font-size: 14px; font-weight: 700; line-height: 17px; text-transform: uppercase;
  }
  .features li { position: relative; padding-left: 15px; }
  .features li::before, .benefits li::before {
    content: ""; position: absolute; left: 0; top: 4px; width: 9px; height: 9px;
    border-radius: 50%; background: var(--red);
  }

  .earnings {
    position: absolute; left: 202px; top: 50px; width: 137px;
    border: 1px solid var(--rule);
    display: grid; grid-template-columns: 58px 1fr;
    font-size: 10px; font-weight: 600;
  }
  .earnings span { height: 17.5px; line-height: 17.5px; padding-left: 4px; border-top: 1px solid var(--rule); }
  .earnings span:nth-child(-n+2) { border-top: none; }
  .earnings span:nth-child(odd) { border-right: 1px solid var(--rule); }
  .earnings b { font-size: 13px; font-weight: 800; }
  .earnings__label {
    position: absolute; left: 225px; top: 28px;
    font-family: "Dancing Script", cursive; font-size: 22px; color: var(--ink);
  }

  .thumb {
    position: absolute; left: 381px; top: 30px; width: 70px; height: 84px;
    border-radius: 14px 14px 4px 4px;
    background: linear-gradient(180deg, #ffffff, #e2e2e2);
    display: flex; flex-direction: column; align-items: center; justify-content: center;
    font-family: "Oswald", sans-serif; font-weight: 600; font-size: 9.5px; line-height: 11px;
  }
  .thumb em { font-style: normal; color: var(--red); }

  /* Footer (shared) */
  .footer { position: absolute; left: 0; top: 595px; width: 100%; height: 105px; }
  .brand {
    position: absolute; left: 18px; top: 12px; width: 104px;
    display: flex; flex-direction: column; align-items: center; gap: 8px;
  }
  .brand__dot { width: 38px; height: 38px; border-radius: 50%; background: var(--red); }
  .brand__name { font-size: 10.5px; font-weight: 800; color: var(--red); white-space: nowrap; }

  .cta { position: absolute; left: 139px; top: 18px; width: 112px; }
  .cta__title { font-family: "Oswald", sans-serif; font-weight: 500; font-size: 14.5px; color: var(--red); line-height: 18px; white-space: nowrap; letter-spacing: -0.2px; }
  .cta__text { width: 100px; font-size: 7.3px; font-weight: 500; line-height: 10px; margin-top: 4px; }
  .cta__text strong { font-weight: 700; }
  .footer__divider { position: absolute; left: 257px; top: 32px; width: 1px; height: 58px; background: #888; }

  .contact { position: absolute; right: 23px; top: 12px; text-align: right; }
  .contact__phone {
    display: flex; align-items: center; justify-content: flex-end; gap: 6px;
    font-size: 22px; font-weight: 800; color: var(--red); line-height: 24px;
  }
  .contact__site { font-size: 14.5px; font-weight: 700; line-height: 19px; }
  .contact__site span { color: var(--red); }
  .contact__row { position: absolute; left: 268px; display: flex; align-items: center; gap: 5px; font-size: 9px; font-weight: 500; white-space: nowrap; }
  .contact__row--mail { top: 62px; }
  .contact__row--post { top: 80px; font-size: 7.2px; }
  .contact__social { margin-left: 10px; }

  /* Back */
  .benefits-title {
    position: absolute; left: 0; top: 40px; width: 100%; text-align: center;
    font-size: 50px; font-weight: 900; color: var(--white); letter-spacing: 1px; line-height: 56px;
  }
  .benefits { position: absolute; top: 168px; list-style: none; font-size: 12px; font-weight: 500; line-height: 14.6px; }
  .benefits li { position: relative; padding-left: 26px; margin-bottom: 7.6px; }
  .benefits li::before { left: 0; top: 3px; }
  .benefits--left { left: 16px; width: 228px; }
  .benefits--right { left: 244px; width: 236px; }
  .benefits--left li:nth-child(6) { margin-bottom: 9px; }
  .benefits--right li:nth-child(6) { margin-bottom: 25px; }

  .promo-shirt { position: absolute; top: 418px; width: 115px; height: 142px; border-radius: 22px 22px 6px 6px; display: flex; align-items: center; justify-content: center; font-weight: 800; font-size: 11px; line-height: 11px; text-align: center; }
  .promo-shirt--white { left: 26px; background: linear-gradient(180deg, #ffffff, #dedede); color: var(--ink); transform: rotate(-6deg); }
  .promo-shirt--black { left: 354px; background: linear-gradient(180deg, #3a3a3a, #1b1b1b); color: var(--white); transform: rotate(6deg); }

  .slogan {
    position: absolute; left: 140px; top: 416px; width: 214px; text-align: center;
    font-size: 32px; font-weight: 900; line-height: 33px; color: var(--ink);
  }
  .slogan__accent { color: var(--red); }
</style>
</head>
<body>

<!-- FRONT -->
<section class="flyer flyer--front" aria-label="Front: T-shirt store fundraiser packages">
  <svg class="flyer__bg" viewBox="0 0 495 700" preserveAspectRatio="none" aria-hidden="true">
    <defs>
      <linearGradient id="front-red" x1="0" y1="0" x2="1" y2="1">
        <stop offset="0" stop-color="#a80c1e"/><stop offset="1" stop-color="#d4162e"/>
      </linearGradient>
      <radialGradient id="front-yellow" cx="0.5" cy="0.5" r="0.7">
        <stop offset="0" stop-color="#ffc61a"/><stop offset="1" stop-color="#f5a800"/>
      </radialGradient>
    </defs>
    <rect width="495" height="700" fill="url(#front-yellow)"/>
    <path d="M0 0H495V226L470 224L440 218L400 214L380 209L340 205L300 196L270 194L230 191L200 186L150 183L120 180L90 177L60 172L30 173L0 168Z" fill="url(#front-red)"/>
    <path d="M0 168L30 173L60 172L90 177L120 180L150 183L200 186L230 191L270 194L300 196L340 205L380 209L400 214L440 218L470 224L495 226V236L470 232L440 228L400 222L380 219L340 214L300 205L270 203L230 199L200 195L150 191L120 188L90 185L60 180L30 181L0 176Z" fill="#ffffff"/>
    <path d="M0 605L40 600L80 598L120 594L170 592L220 586L260 584L310 580L350 578L400 574L450 570L495 565V700H0Z" fill="#ffffff"/>
  </svg>

  <h1 class="headline">BUILD YOUR<br><span class="headline__accent">TSHIRT STORE</span><br>FUNDRAISER</h1>
  <div class="hero-shirts" role="img" aria-label="Photo of a white and a black T-shirt printed with the shop name"></div>

  <div class="package package--silver">
    <div class="tier tier--silver">Silver</div>
    <ul class="features"><li>2 Shirt Choice</li><li>1 Design</li><li>1 Color</li></ul>
    <div class="earnings__label">Sell</div>
    <div class="earnings"><span>1-25</span><span>EARN <b>20%</b></span><span>25-50</span><span>EARN <b>25%</b></span><span>50-100</span><span>EARN <b>30%</b></span></div>
    <div class="thumb" role="img" aria-label="Photo of a white T-shirt mockup">YOUR<em>DESIGN</em>HERE</div>
  </div>

  <div class="package package--gold">
    <div class="tier tier--gold">Gold</div>
    <ul class="features"><li>2 Shirt Choice</li><li>2 Designs</li><li>3 Colors</li></ul>
    <div class="earnings__label">Sell</div>
    <div class="earnings"><span>1-25</span><span>EARN <b>15%</b></span><span>25-50</span><span>EARN <b>20%</b></span><span>50-100</span><span>EARN <b>25%</b></span></div>
    <div class="thumb" role="img" aria-label="Photo of a white T-shirt mockup">YOUR<em>DESIGN</em>HERE</div>
  </div>

  <div class="package package--platinum">
    <div class="tier tier--platinum">Platinum</div>
    <ul class="features"><li>4 Shirt/Hoodie<br>Choice</li><li>3 Designs</li><li>Unlmt Colors</li></ul>
    <div class="earnings__label">Sell</div>
    <div class="earnings"><span>1-25</span><span>EARN <b>10%</b></span><span>25-50</span><span>EARN <b>15%</b></span><span>50-100</span><span>EARN <b>20%</b></span></div>
    <div class="thumb" role="img" aria-label="Photo of a white T-shirt mockup">YOUR<em>DESIGN</em>HERE</div>
  </div>

  <footer class="footer">
    <div class="brand"><span class="brand__dot"></span><span class="brand__name">LANTERN PRINT CO</span></div>
    <div class="cta">
      <p class="cta__title">CONTACT US NOW !</p>
      <p class="cta__text">To build your free store to earn money for your organization or group!<br><strong>CALL FOR MORE INFO!</strong></p>
    </div>
    <div class="footer__divider"></div>
    <div class="contact">
      <p class="contact__phone"><svg width="16" height="16" viewBox="0 0 24 24" aria-hidden="true"><path fill="#1c1c1c" d="M6.6 10.8a15.1 15.1 0 0 0 6.6 6.6l2.2-2.2c.3-.3.7-.4 1-.2 1.1.4 2.3.6 3.6.6.6 0 1 .4 1 1V20c0 .6-.4 1-1 1A17 17 0 0 1 3 4c0-.6.4-1 1-1h3.5c.6 0 1 .4 1 1 0 1.3.2 2.5.6 3.6.1.3 0 .7-.2 1z"/></svg>555-204-7781</p>
      <p class="contact__site">www.<span>lanternprintco</span>.com</p>
    </div>
    <p class="contact__row contact__row--mail"><svg width="11" height="8" viewBox="0 0 22 16" aria-hidden="true"><path fill="#1c1c1c" d="M0 0h22v16H0zM2 2v.5l9 6 9-6V2zm0 3v9h18V5l-9 6z"/></svg>hello@lanternprintco.com<span class="contact__social">@lanternprintco</span></p>
    <p class="contact__row contact__row--post"><svg width="8" height="11" viewBox="0 0 16 22" aria-hidden="true"><path fill="#1c1c1c" d="M8 0a8 8 0 0 1 8 8c0 6-8 14-8 14S0 14 0 8a8 8 0 0 1 8-8zm0 5a3 3 0 1 0 0 6 3 3 0 0 0 0-6z"/></svg>Lantern Print Co P O Box 612 Lakeview, MI, 48000</p>
  </footer>
</section>

<!-- BACK -->
<section class="flyer flyer--back" aria-label="Back: benefits of the fundraiser store">
  <svg class="flyer__bg" viewBox="0 0 495 700" preserveAspectRatio="none" aria-hidden="true">
    <defs>
      <linearGradient id="back-red" x1="0" y1="0" x2="1" y2="1">
        <stop offset="0" stop-color="#a80c1e"/><stop offset="1" stop-color="#d4162e"/>
      </linearGradient>
      <radialGradient id="back-yellow" cx="0.5" cy="0.5" r="0.7">
        <stop offset="0" stop-color="#ffc61a"/><stop offset="1" stop-color="#f5a800"/>
      </radialGradient>
    </defs>
    <rect width="495" height="700" fill="url(#back-yellow)"/>
    <path d="M0 0H495V142L470 146L440 152L410 150L380 146L350 140L320 138L290 130L250 124L210 120L180 116L150 114L110 110L70 106L40 100L0 104Z" fill="url(#back-red)"/>
    <path d="M0 104L40 100L70 106L110 110L150 114L180 116L210 120L250 124L290 130L320 138L350 140L380 146L410 150L440 152L470 146L495 142V151L470 155L440 160L410 158L380 154L350 148L320 146L290 139L250 132L210 128L180 124L150 122L110 118L70 114L40 108L0 112Z" fill="#ffffff"/>
    <path d="M0 580L50 574L100 572L150 568L200 566L250 562L300 562L350 558L400 556L450 554L495 550V700H0Z" fill="#ffffff"/>
  </svg>

  <h2 class="benefits-title">BENEFITS</h2>

  <ul class="benefits benefits--left">
    <li>No stock</li>
    <li>No order form</li>
    <li>Daily order summary</li>
    <li>No customer contact<br>(covid approved)</li>
    <li>No headaches</li>
    <li>Invest less time with sales and more time connecting with your audience to invest in a worthy cause</li>
    <li>Online platform</li>
  </ul>
  <ul class="benefits benefits--right">
    <li>No upfront cost</li>
    <li>Instant order notification</li>
    <li>No money exchange/collecting</li>
    <li>No risk</li>
    <li>Tshirts are an easy sale for the right purpose</li>
    <li>All fullfillment and shipping handled by lantern print co</li>
    <li>Gain revenue for your organization</li>
  </ul>

  <div class="promo-shirt promo-shirt--white" role="img" aria-label="Photo of a white T-shirt mockup">YOUR<br>LOGO<br>HERE</div>
  <p class="slogan">WIN WIN<br><span class="slogan__accent">SITUATION</span><br>YOU CANT<br><span class="slogan__accent">LOSE</span></p>
  <div class="promo-shirt promo-shirt--black" role="img" aria-label="Photo of a black T-shirt mockup">YOUR<br>LOGO<br>HERE</div>

  <footer class="footer">
    <div class="brand"><span class="brand__dot"></span><span class="brand__name">LANTERN PRINT CO</span></div>
    <div class="cta">
      <p class="cta__title">CONTACT US NOW !</p>
      <p class="cta__text">To build your free store to earn money for your organization or group!<br><strong>CALL FOR MORE INFO!</strong></p>
    </div>
    <div class="footer__divider"></div>
    <div class="contact">
      <p class="contact__phone"><svg width="16" height="16" viewBox="0 0 24 24" aria-hidden="true"><path fill="#1c1c1c" d="M6.6 10.8a15.1 15.1 0 0 0 6.6 6.6l2.2-2.2c.3-.3.7-.4 1-.2 1.1.4 2.3.6 3.6.6.6 0 1 .4 1 1V20c0 .6-.4 1-1 1A17 17 0 0 1 3 4c0-.6.4-1 1-1h3.5c.6 0 1 .4 1 1 0 1.3.2 2.5.6 3.6.1.3 0 .7-.2 1z"/></svg>555-204-7781</p>
      <p class="contact__site">www.<span>lanternprintco</span>.com</p>
    </div>
    <p class="contact__row contact__row--mail"><svg width="11" height="8" viewBox="0 0 22 16" aria-hidden="true"><path fill="#1c1c1c" d="M0 0h22v16H0zM2 2v.5l9 6 9-6V2zm0 3v9h18V5l-9 6z"/></svg>hello@lanternprintco.com<span class="contact__social">@lanternprintco</span></p>
    <p class="contact__row contact__row--post"><svg width="8" height="11" viewBox="0 0 16 22" aria-hidden="true"><path fill="#1c1c1c" d="M8 0a8 8 0 0 1 8 8c0 6-8 14-8 14S0 14 0 8a8 8 0 0 1 8-8zm0 5a3 3 0 1 0 0 6 3 3 0 0 0 0-6z"/></svg>Lantern Print Co P O Box 612 Lakeview, MI, 48000</p>
  </footer>
</section>

</body>
</html>
```